Lawn mowing business card design

We need a business card design for our lawn mowing and gardening business which is located in the Northern Beaches of Sydney. Our business name is Meadowline Turf and our logo is predominantly green and yellow in color. Please see our website at www.meadowlineturf.com.au for design ideas. The business targets young professionals and older clientele. As such the font should be easy to read, but I also want the business card to be colorful and stand out.

Target Market(s)

young professionals

Industry/Entity Type

Lawn Care

Contact Information for Business Card

Meadowline Turf, Gareth Pellow, 0478559201, www.meadowlineturf.com.au, email: meadowlineturf@mailbox-example.com

Font styles to use
Serif

Colors
9bcb3b
fbed22

Requirements
Must have
• Must include the details listed above. Must include the attached logo.
Nice to have
• Logo attached with two copies. The logo without any writing is high quality, please feel free to be creative with the text stating our business name "Meadowline Turf" using this file.

```html
<!DOCTYPE html>
<html lang="en">
<head>
<meta charset="utf-8">
<title>Meadowline Turf – Business Card</title>
<link href="https://fonts.googleapis.com/css2?family=Lato:wght@300;400;700;900&display=swap" rel="stylesheet">
<style>
  :root{
    --stage:#e9ebe6;
    --charcoal:#2f2e2f;
    --grass:#3d9b35;
    --grass-light:#6cb943;
    --grass-dark:#1f6e2a;
    --sun:#f2d21d;
    --paper:#f7f7f5;
    --ink:#232323;
    --muted:#d9d9d9;
    --rule:#4a4a4a;
  }
  *{box-sizing:border-box;margin:0;padding:0}
  html,body{width:1200px;height:800px;overflow:hidden}
  body{background:var(--stage);font-family:"Lato",Arial,sans-serif;position:relative}

  .card{position:absolute;top:137px;width:320px;height:525px;overflow:hidden;
        box-shadow:0 10px 28px rgba(0,0,0,.22);background:var(--charcoal)}
  .card--front{left:210px}
  .card--back{left:670px}
  .card__bg{position:absolute;inset:0}

  .mascot{position:absolute;border-radius:14px;
          background:linear-gradient(135deg,var(--grass-light) 0%,var(--sun) 55%,var(--grass) 100%)}
  .card--front .mascot{left:70px;top:215px;width:180px;height:140px}
  .card--back .mascot{left:95px;top:28px;width:130px;height:100px}

  .brand-name{position:absolute;left:0;right:0;text-align:center;font-weight:900;letter-spacing:.5px}
  .card--front .brand-name{top:372px;font-size:27px;color:var(--paper)}
  .card--back .brand-name{top:140px;font-size:20px;color:var(--ink)}

  .holder{position:absolute;left:26px;top:228px;color:#fff;font-size:14px;
          font-weight:400;letter-spacing:1.5px;text-transform:uppercase}

  .contacts{position:absolute;left:30px;right:24px;top:300px;list-style:none}
  .contact{display:flex;align-items:center;gap:14px;height:56px;border-bottom:1px solid var(--rule);
           color:var(--muted);font-size:13px;font-weight:300}
  .contact:last-child{border-bottom:none}
  .contact__icon{flex:none;width:26px;height:26px;border:1.5px solid var(--grass);
                 display:flex;align-items:center;justify-content:center}
</style>
</head>
<body>

<!-- Front -->
<section class="card card--front">
  <svg class="card__bg" viewBox="0 0 320 525" width="320" height="525" aria-hidden="true">
    <rect width="320" height="525" fill="var(--charcoal)"/>
    <polygon points="0,0 205,0 0,420" fill="var(--grass)"/>
  </svg>
  <div class="mascot" role="img" aria-label="Cartoon lawn mower mascot illustration"></div>
  <p class="brand-name">Meadowline Turf</p>
</section>

<!-- Back -->
<section class="card card--back">
  <svg class="card__bg" viewBox="0 0 320 525" width="320" height="525" aria-hidden="true">
    <rect width="320" height="525" fill="var(--charcoal)"/>
    <polygon points="0,0 320,0 320,150 0,270" fill="var(--paper)"/>
    <polygon points="0,205 262,205 242,270 0,270" fill="var(--grass)"/>
    <polygon points="0,210 255,210 238,264 0,264" fill="none" stroke="var(--grass-dark)" stroke-width="2"/>
    <circle cx="232" cy="237" r="19" fill="#fff"/>
    <circle cx="232" cy="231" r="6" fill="var(--grass)"/>
    <path d="M221 249 q11 -14 22 0 z" fill="var(--grass)"/>
  </svg>
  <div class="mascot" role="img" aria-label="Cartoon lawn mower mascot illustration"></div>
  <p class="brand-name">Meadowline Turf</p>
  <p class="holder">Gareth Pellow</p>

  <ul class="contacts">
    <li class="contact">
      <span class="contact__icon">
        <svg width="14" height="14" viewBox="0 0 24 24" aria-hidden="true"><path d="M6.6 10.8a15 15 0 006.6 6.6l2.2-2.2a1 1 0 011-.25 11.4 11.4 0 003.6.6 1 1 0 011 1V20a1 1 0 01-1 1A17 17 0 013 4a1 1 0 011-1h3.5a1 1 0 011 1 11.4 11.4 0 00.6 3.6 1 1 0 01-.25 1z" fill="#fff"/></svg>
      </span>
      0478559201
    </li>
    <li class="contact">
      <span class="contact__icon">
        <svg width="14" height="14" viewBox="0 0 24 24" aria-hidden="true"><rect x="2" y="5" width="20" height="14" fill="#fff"/><path d="M2 5l10 8 10-8" fill="none" stroke="var(--charcoal)" stroke-width="2"/></svg>
      </span>
      meadowlineturf@mailbox-example.com
    </li>
    <li class="contact">
      <span class="contact__icon">
        <svg width="14" height="14" viewBox="0 0 24 24" aria-hidden="true"><circle cx="12" cy="12" r="10" fill="none" stroke="#fff" stroke-width="2"/><ellipse cx="12" cy="12" rx="4" ry="10" fill="none" stroke="#fff" stroke-width="2"/><path d="M2 12h20M4 7h16M4 17h16" stroke="#fff" stroke-width="1.5"/></svg>
      </span>
      www.meadowlineturf.com.au
    </li>
  </ul>
</section>

</body>
</html>
```